Ridgemont Business Card Redesign

Using the current logo/tagline lock-up and icon, redesign the Ridgemont business card to better show the tagline and improve the layout to give the card a more timely design and a classic, sophisticated look. See attached Project Brief for more detail.

```html
<!DOCTYPE html>
<html lang="en">
<head>
<meta charset="utf-8">
<title>Ridgemont Capital – Business Card</title>
<link href="https://fonts.googleapis.com/css2?family=Raleway:wght@400;500;600&display=swap" rel="stylesheet">
<style>
  :root {
    --backdrop-deep: #03355a;
    --backdrop-light: #0b4a7c;
    --card-white: #ffffff;
    --brand-blue: #1473c1;
    --panel-charcoal: #3c3c3e;
    --ink-dark: #333438;
    --ink-mid: #47484c;
    --on-dark: #ffffff;
  }
  html, body {
    margin: 0;
    width: 1200px;
    height: 1200px;
    overflow: hidden;
  }
  body {
    background: radial-gradient(circle at 50% 55%, var(--backdrop-light), var(--backdrop-deep) 75%);
    font-family: "Raleway", sans-serif;
  }
  .business-card {
    position: absolute;
    left: 100px;
    top: 308px;
    width: 1000px;
    height: 583px;
    background: var(--card-white);
    overflow: hidden;
    box-shadow: 0 10px 30px rgba(0,0,0,0.25);
  }
  .card-shapes {
    position: absolute;
    inset: 0;
  }
  .brand-lockup {
    position: absolute;
    left: 40px;
    top: 70px;
    display: flex;
    align-items: center;
    gap: 18px;
  }
  .brand-dot {
    width: 70px;
    height: 70px;
    border-radius: 50%;
    background: var(--brand-blue);
  }
  .brand-name {
    font-size: 42px;
    font-weight: 500;
    color: var(--ink-dark);
    letter-spacing: 1px;
  }
  .holder {
    position: absolute;
    right: 44px;
    top: 62px;
    text-align: right;
  }
  .holder-name {
    margin: 0;
    font-size: 40px;
    font-weight: 600;
    color: var(--brand-blue);
    line-height: 1.2;
  }
  .holder-rule {
    position: absolute;
    left: 629px;
    top: 122px;
    width: 371px;
    height: 3px;
    background: var(--brand-blue);
  }
  .holder-title {
    position: absolute;
    right: 44px;
    top: 130px;
    margin: 0;
    text-align: right;
    font-size: 26px;
    line-height: 34px;
    color: var(--ink-mid);
  }
  .contact-list {
    position: absolute;
    right: 50px;
    top: 312px;
    margin: 0;
    padding: 0;
    list-style: none;
  }
  .contact-list li {
    display: flex;
    justify-content: flex-end;
    align-items: center;
    gap: 14px;
    height: 37.5px;
    font-size: 23px;
    color: var(--on-dark);
  }
  .contact-icon {
    width: 22px;
    height: 22px;
    fill: var(--brand-blue);
  }
  .address {
    position: absolute;
    left: 48px;
    top: 400px;
    display: flex;
    gap: 14px;
    font-size: 23px;
    line-height: 31px;
    color: var(--ink-dark);
  }
  .address-pin {
    width: 22px;
    height: 28px;
    fill: var(--brand-blue);
    margin-top: 2px;
  }
  .website {
    position: absolute;
    right: 47px;
    top: 508px;
    font-size: 23px;
    letter-spacing: 4px;
    color: var(--on-dark);
  }
</style>
</head>
<body>
  <article class="business-card">
    <svg class="card-shapes" width="1000" height="583" viewBox="0 0 1000 583" aria-hidden="true">
      <path class="contact-panel" d="M1000 266 L622 266 Q570 266 550 312 L470 498 L1000 498 Z" fill="var(--panel-charcoal)"/>
      <rect class="footer-band" x="0" y="498" width="1000" height="85" fill="var(--brand-blue)"/>
    </svg>

    <div class="brand-lockup">
      <span class="brand-dot"></span>
      <span class="brand-name">Ridgemont Capital</span>
    </div>

    <div class="holder">
      <h1 class="holder-name">Daniel R. Whitaker</h1>
    </div>
    <div class="holder-rule"></div>
    <p class="holder-title">Principal &amp;<br>Chief Marketing Officer</p>

    <ul class="contact-list">
      <li>(555) 210-4831
        <svg class="contact-icon" viewBox="0 0 24 24"><path d="M6.6 10.8a15.1 15.1 0 0 0 6.6 6.6l2.2-2.2a1 1 0 0 1 1-.25 11.4 11.4 0 0 0 3.6.57 1 1 0 0 1 1 1V20a1 1 0 0 1-1 1A17 17 0 0 1 3 4a1 1 0 0 1 1-1h3.5a1 1 0 0 1 1 1c0 1.25.2 2.45.57 3.57a1 1 0 0 1-.25 1z"/></svg>
      </li>
      <li>(000) 000 0000
        <svg class="contact-icon" viewBox="0 0 24 24"><path d="M6.6 10.8a15.1 15.1 0 0 0 6.6 6.6l2.2-2.2a1 1 0 0 1 1-.25 11.4 11.4 0 0 0 3.6.57 1 1 0 0 1 1 1V20a1 1 0 0 1-1 1A17 17 0 0 1 3 4a1 1 0 0 1 1-1h3.5a1 1 0 0 1 1 1c0 1.25.2 2.45.57 3.57a1 1 0 0 1-.25 1z"/></svg>
      </li>
      <li>(555) 318-7702
        <svg class="contact-icon" viewBox="0 0 24 24"><path d="M7 1h10a2 2 0 0 1 2 2v18a2 2 0 0 1-2 2H7a2 2 0 0 1-2-2V3a2 2 0 0 1 2-2zm0 3v14h10V4zm5 15.2a1 1 0 1 0 0 2 1 1 0 0 0 0-2z"/></svg>
      </li>
      <li>dwhitaker@ridgemontcapital.com
        <svg class="contact-icon" viewBox="0 0 24 24"><path d="M2 5h20v2l-10 6L2 7zm0 4.3 10 6 10-6V19H2z"/></svg>
      </li>
    </ul>

    <div class="address">
      <svg class="address-pin" viewBox="0 0 24 30"><path d="M12 0a11 11 0 0 0-11 11c0 8 11 19 11 19s11-11 11-19A11 11 0 0 0 12 0zm0 15.5a4.5 4.5 0 1 1 0-9 4.5 4.5 0 0 1 0 9z"/></svg>
      <p style="margin:0">41 Alder Park Road,<br>Suite 210 Norwalk, CT 06850</p>
    </div>

    <div class="website">www.ridgemontcapital.com</div>
  </article>
</body>
</html>
```